Brochure for a paper wholesaler who wants to educate his print industry clients

We will be making a stapled informative brochure, that contains basic information about our paper products - the types of paper there is, their characteristics and other useful information.
As we are part of a paper wholesaler group in Europe - VORENT, we received a brochure in German that has this kind of information. The text in it is not as important. What is important is the layout of the document and how the text will appear in it (added in the uploaded files - 210915_Wiessenswertes_TBLK_F51.pdf).
We are allowed to tinker with this file and adjust it to our needs. So there are also .idml and .indd files available (also in the uploaded files).
We would like to keep the custom page size of 210 x290mm (8.3x11.4 in), or you can go up to 210x297mm (8.3x11.7 in).
What we want is a modern looking design that contains our companies red bordo and white/ grey colours to replace the existing green colours in this borchure. The pictures and appearance of the file can be changed according to your views and what you think would look good. We don't necessarily want to keep the same design, we just want the layout of the document be the same, as we will be placing our translated text into it. The VORENT logo should be replaced with our own logo (KUMET Logo.png).
As for how it could look, it could go together with our paper presentation, for which the design can be seen in the "KUMET Base - v2.pptx".
Holiday season, so have a lot of tasks to take care of and not as much time to check ArtHarbor as often.

```html
<!DOCTYPE html>
<html lang="de">
<head>
<meta charset="utf-8">
<title>Wissenswertes – Papier und Formate</title>
<link href="https://fonts.googleapis.com/css2?family=Source+Sans+3:wght@400;600;700&display=swap" rel="stylesheet">
<style>
:root{
  --bordo:#8b2a2f;
  --ink:#222;
  --page:#ffffff;
  --stage:#ececec;
  --grey-dark:#d6d6d6;
  --grey-mid:#e3e3e3;
  --grey-light:#efefef;
  --photo-dark:#5b5d63;
  --photo-light:#c9c7c2;
}
*{margin:0;padding:0;box-sizing:border-box}
html,body{width:1200px;height:1000px;overflow:hidden;background:var(--stage)}
body{font-family:"Source Sans 3",Arial,sans-serif;color:var(--ink);position:relative}
.page{position:absolute;top:92px;height:816px;background:var(--page);overflow:hidden}
.page-left{left:10px;width:590px}
.page-right{left:600px;width:590px}
.abs{position:absolute}
.section-title{position:absolute;font-size:20px;font-weight:600;color:var(--bordo);line-height:1}
.sub-title{position:absolute;font-size:10px;font-weight:700;line-height:1}
.body-text{position:absolute;font-size:10.2px;line-height:14px;white-space:nowrap}
.fmt-list{position:absolute;font-size:9.8px;line-height:18.6px;list-style:none}
.fmt-list li{display:flex}
.fmt-list .key{font-weight:700;width:36px;position:relative}
.fmt-list .key.star::before{content:"*";position:absolute;left:-6px}
.note{position:absolute;font-size:9.8px}

/* Karton table */
.board-table{position:absolute;left:47px;top:89px;width:500px;border-collapse:collapse;table-layout:fixed;font-size:9.3px;line-height:11.5px;text-align:center}
.board-table th{background:var(--bordo);color:#fff;font-weight:600;height:27px;border:1px solid #fff}
.board-table td{border:1px solid #fff;padding:0 2px;background:var(--grey-light)}
.board-table td.group{background:var(--grey-dark);font-weight:700}
.board-table tr.shade td:not(.group){background:var(--grey-mid)}

/* thickness table */
.thick-table{position:absolute;left:41px;top:349px;width:501px;border-collapse:collapse;table-layout:fixed;font-size:9.5px;text-align:center}
.thick-table th{background:var(--bordo);color:#fff;font-weight:400;height:28px;line-height:11px;border-left:1px solid #fff}
.thick-table th b{font-weight:700}
.thick-table td{height:18.1px;border-left:1px solid #fff}
.thick-table tr:nth-child(odd) td{background:var(--grey-mid)}
.thick-table tr:nth-child(even) td{background:var(--grey-light)}
.thick-table td:first-child{font-weight:700}
.thick-table th:first-child{width:108px}

.formula{position:absolute;left:41px;top:625px;font-size:9.5px}
.formula .lhs{position:absolute;left:0;top:10px;white-space:nowrap}
.formula .num{position:absolute;left:45px;top:0;width:336px;text-align:center;white-space:nowrap;border-bottom:1px solid var(--ink);padding-bottom:3px}
.formula .den{position:absolute;left:45px;top:19px;width:336px;text-align:center}

.legal{position:absolute;left:562px;top:800px;transform:rotate(-90deg);transform-origin:left top;font-size:6px;color:#777;white-space:nowrap}

.brand-name{position:absolute;left:400px;top:748px;color:#fff;font-size:22px;font-weight:400;line-height:1}
</style>
</head>
<body>

<section class="page page-left">
  <h2 class="section-title" style="left:46px;top:45px">Karton im Überblick</h2>

  <table class="board-table">
    <colgroup><col style="width:84px"><col style="width:78px"><col style="width:101px"><col style="width:79px"><col style="width:80px"><col style="width:78px"></colgroup>
    <tr><th colspan="2"></th><th>Strich</th><th>Bekannte Bezeichnung</th><th>Kurz-<br>bezeichnung</th><th>Englische Bezeichnung</th></tr>
    <tr class="shade" style="height:41px"><td class="group" rowspan="2">Chromo-<br>Sulfatkarton</td><td>Gebleicht –<br>weiß, gestrichen</td><td>Einseitig oder zwei-<br>seitig zweifach<br>gestrichen</td><td>Sulfatkarton=<br>Zellstoffkarton</td><td>GZ, gestrichener Zellstoffkarton</td><td>SBS board, Solid Bleached Sulfat Board</td></tr>
    <tr style="height:81px"><td>Ungebleicht –<br>braun,<br>gestrichen</td><td>Einseitig oder<br>zweiseitig gestrichen</td><td>Kraftkarton</td><td>GN 4,<br>gestrichener,<br>ungebleichter<br>Zellstoffkarton<br>mit brauner<br>Rückseite</td><td>CNK, Coated<br>Natural Kraft<br>SUB, Solid<br>Unbleached<br>Board</td></tr>
    <tr class="shade" style="height:40px"><td class="group" rowspan="2">Chromokarton</td><td>Mit gestrichener<br>weißer<br>Rückseite</td><td>Einfach gestrichene Rückseite, Vorderseite zweifach gestrichen</td><td>Faltschachtel-<br>karton</td><td>GC 1,<br>gestrichener<br>Chromokarton</td><td>FBB, Folding Box Board coated<br>1 side</td></tr>
    <tr style="height:41px"><td>Mit ungestri-<br>chener heller<br>Rückseite</td><td>Helle, ungestrichene Rückseite, Vorderseite zweifach gestrichen</td><td>Faltschachtel-<br>karton</td><td>GC 2,<br>gestrichener<br>Chromokarton 2</td><td>FBB, Folding<br>Box Board with<br>manilla back</td></tr>
    <tr class="shade" style="height:42px"><td class="group">Chromo-<br>Duplexkarton</td><td>Mit grauer<br>Rückseite</td><td>Rückseite pigmen-<br>tiert, Vorderseite<br>zweifach gestrichen</td><td>Duplexkarton</td><td>GD 2,<br>gestrichener<br>Duplexkarton 2</td><td>WLC,<br>White Lined<br>Chipboard</td></tr>
  </table>

  <h2 class="section-title" style="left:46px;top:391px">Das kleine 1x1 der Formatschule</h2>
  <h3 class="sub-title" style="left:47px;top:435px">Bogen-, DIN- und VORENT Lagerformate</h3>
  <p class="body-text" style="left:47px;top:452px">Papierformate sind nach DIN genormt. Das Urformat der Reihe A ist ein Rechteck von 1 qm Größe.<br>Jedes weitere Format ergibt sich durch Halbieren oder Verdoppeln und hat ein Seitenverhältnis von 1:√2. Aus der<br>DIN-Reihe A sind die DIN-Reihen B, C, und D abgeleitet. Die Rohformate, zur DIN-A-Reihe passend, werden ebenfalls als<br>geläufige Formate gehandelt.</p>

  <h3 class="sub-title" style="left:47px;top:523px">DIN-A-Formate</h3>
  <ul class="fmt-list" style="left:47px;top:537px">
    <li><span class="key">A0</span>841 x 1.189 mm</li>
    <li><span class="key">A1</span>594 x 841 mm</li>
    <li><span class="key">A2</span>420 x 595 mm</li>
    <li><span class="key">A3</span>297 x 420 mm</li>
    <li><span class="key">A4</span>210 x 297 mm</li>
    <li><span class="key">A5</span>128 x 210 mm</li>
    <li><span class="key">A6</span>105 x 148 mm</li>
    <li><span class="key">A7</span>74 x 105 mm</li>
  </ul>

  <h3 class="sub-title" style="left:261px;top:523px">DIN-B-Formate</h3>
  <ul class="fmt-list" style="left:261px;top:537px">
    <li><span class="key">B0</span>1.000 x 1.414 mm</li>
    <li><span class="key">B1</span>707 x 1.000 mm</li>
    <li><span class="key">B2</span>500 x 707 mm</li>
    <li><span class="key">B3</span>353 x 500 mm</li>
    <li><span class="key star">B4</span>250 x 353 mm</li>
    <li><span class="key star">B5</span>176 x 250 mm</li>
    <li><span class="key star">B6</span>125 x 176 mm</li>
    <li><span class="key">B7</span>88 x 125 mm</li>
  </ul>
  <p class="note" style="left:260px;top:707px">*Briefhüllen-/Versandtaschenformat</p>

  <p class="legal">Änderungen und Irrtümer vorbehalten.</p>
</section>

<section class="page page-right">
  <h3 class="sub-title" style="left:41px;top:47px">DIN-C-Formate</h3>
  <ul class="fmt-list" style="left:41px;top:61px">
    <li><span class="key">C0</span>917 x 1.297 mm</li>
    <li><span class="key">C1</span>648 x 917 mm</li>
    <li><span class="key">C2</span>458 x 648 mm</li>
    <li><span class="key">C3</span>324 x 458 mm</li>
    <li><span class="key star">C4</span>229 x 324 mm</li>
    <li><span class="key star">C5</span>162 x 229 mm</li>
    <li><span class="key star">C6</span>114 x 162 mm</li>
  </ul>

  <h3 class="sub-title" style="left:257px;top:47px">DIN-lang</h3>
  <ul class="fmt-list" style="left:260px;top:61px">
    <li><span class="key star" style="width:35px">DL</span>220 x 110 mm</li>
  </ul>
  <p class="note" style="left:254px;top:102px">*Briefhüllen-/Versandtaschenformat</p>

  <svg class="abs" style="left:440px;top:42px" width="120" height="106" viewBox="0 0 120 106" role="img" aria-label="Briefhüllen-Symbol">
    <g fill="#fff" stroke="#555" stroke-width="0.8">
      <rect x="22" y="2" width="70" height="56"/>
      <rect x="44" y="30" width="70" height="52"/>
      <rect x="12" y="48" width="72" height="44"/>
      <rect x="38" y="68" width="68" height="36"/>
    </g>
    <circle cx="28" cy="38" r="24" fill="var(--bordo)"/>
    <g fill="none" stroke="#fff" stroke-width="1.6">
      <rect x="17" y="30" width="22" height="15"/>
      <path d="M17 30 L28 39 L39 30"/>
    </g>
  </svg>

  <h3 class="sub-title" style="left:258px;top:159px">Rohformate, unbeschnitten</h3>
  <ul class="fmt-list" style="left:258px;top:173px">
    <li><span class="key">A0</span>860 x 1.120 mm</li>
    <li><span class="key">A1</span>610 x 860 mm</li>
    <li><span class="key">A2</span>430 x 610 mm</li>
    <li><span class="key">A3</span>305 x 430 mm</li>
  </ul>

  <h2 class="section-title" style="left:41px;top:283px">Umfangreiche Sache</h2>

  <table class="thick-table">
    <tr><th>Papiergewicht g/qm</th><th><b>1,0-fach</b><br>100 Blatt</th><th><b>1,3-fach</b><br>100 Blatt</th><th><b>1,5-fach</b><br>100 Blatt</th><th><b>1,8-fach</b><br>100 Blatt</th><th><b>2,0-fach</b><br>100 Blatt</th><th><b>2,2-fach</b><br>100 Blatt</th><th><b>2,5-fach</b><br>100 Blatt</th></tr>
    <tr><td>60</td><td>6,0</td><td>7,8</td><td>9,0</td><td>10,8</td><td>12,0</td><td>13,2</td><td>15,0</td></tr>
    <tr><td>70</td><td>7,0</td><td>9,1</td><td>10,5</td><td>12,6</td><td>14,0</td><td>15,4</td><td>17,5</td></tr>
    <tr><td>80</td><td>8,0</td><td>10,4</td><td>12,0</td><td>14,4</td><td>16,0</td><td>17,6</td><td>20,0</td></tr>
    <tr><td>90</td><td>9,0</td><td>11,7</td><td>13,5</td><td>16,2</td><td>18,0</td><td>19,8</td><td>22,5</td></tr>
    <tr><td>100</td><td>10,0</td><td>13,0</td><td>15,0</td><td>18,0</td><td>20,0</td><td>22,0</td><td>25,0</td></tr>
    <tr><td>110</td><td>11,0</td><td>14,3</td><td>16,5</td><td>19,8</td><td>22,0</td><td>24,2</td><td>27,5</td></tr>
    <tr><td>120</td><td>12,0</td><td>15,6</td><td>18,0</td><td>21,6</td><td>24,0</td><td>26,4</td><td>30,0</td></tr>
    <tr><td>135</td><td>13,5</td><td>17,6</td><td>20,3</td><td>24,3</td><td>27,0</td><td>29,7</td><td>33,8</td></tr>
    <tr><td>150</td><td>15,0</td><td>19,5</td><td>22,5</td><td>27,0</td><td>30,0</td><td>33,0</td><td>37,5</td></tr>
    <tr><td>170</td><td>17,0</td><td>22,1</td><td>25,5</td><td>30,6</td><td>34,0</td><td>37,4</td><td>42,5</td></tr>
    <tr><td>200</td><td>20,0</td><td>26,0</td><td>30,0</td><td>36,0</td><td>40,0</td><td>44,0</td><td>50,0</td></tr>
  </table>

  <h3 class="sub-title" style="left:41px;top:607px">Berechnung der Dicke des Buchblocks (D)</h3>
  <div class="formula">
    <span class="lhs">D (mm)=</span>
    <span class="num">Blattzahl x Quadratmetergewicht (g/qm) x Volumen des Papiers (1,x-fach)</span>
    <span class="den">1.000</span>
  </div>

  <svg class="abs" style="left:0;top:0" width="590" height="816" viewBox="0 0 590 816" role="img" aria-label="Foto: gestapelte Papierbögen und Broschüren">
    <defs>
      <linearGradient id="paperStack" x1="0" y1="1" x2="1" y2="0">
        <stop offset="0" stop-color="var(--photo-dark)"/>
        <stop offset="0.55" stop-color="#9a9894"/>
        <stop offset="1" stop-color="var(--photo-light)"/>
      </linearGradient>
    </defs>
    <polygon points="0,753 590,620 590,816 0,816" fill="url(#paperStack)"/>
  </svg>

  <span class="brand-name">KUMET</span>
</section>

</body>
</html>
```